Freelance business trainer needs a new business card

My business is called Brightpath. I provide training in the workplace on management, coaching and mentoring, and customer service topics for a variety of businesses, colleges and private training providers, and teach on management programs. I need a professional but eye catching business card. Business colours grey and orange. My name Linda Marrowby; Tel 07862 413057; email lmarrowby@brightpath.co.uk; website www.brightpath.co.uk.
Happy to have some sort of logo on front and details on back or all on one side
Target Market(s)
SME businesses and colleges - workshops i run are for adults in the workplace
Industry/Entity Type
Training
Look and feel
Each slider illustrates characteristics of the customer's brand and the style your logo design should communicate.

```html
<!DOCTYPE html>
<html lang="en">
<head>
<meta charset="utf-8">
<title>Brightpath business card</title>
<link rel="stylesheet" href="https://fonts.googleapis.com/css2?family=Arimo:wght@400;700&family=Questrial&display=swap">
<style>
  :root {
    --orange: #ff8a00;
    --orange-soft: #ffb155;
    --ink: #444446;
    --tagline: #3a3a3a;
    --stage: #e5e5e5;
    --card-back: #cacaca;
    --white: #ffffff;
    --shadow: rgba(0, 0, 0, 0.28);
  }
  * { margin: 0; padding: 0; box-sizing: border-box; }
  html, body {
    width: 1200px;
    height: 591px;
    overflow: hidden;
    background: var(--stage);
  }
  .stage {
    position: relative;
    width: 1200px;
    height: 591px;
    background: var(--stage);
  }
  .card {
    position: absolute;
    width: 442px;
    height: 270px;
    top: 139px;
    box-shadow: 22px 18px 22px var(--shadow);
    overflow: hidden;
  }
  .card--front { left: 83px; background: var(--white); }
  .card--back { left: 635px; background: var(--card-back); }

  .front-art {
    position: absolute;
    inset: 0;
    width: 442px;
    height: 270px;
  }

  .brand {
    position: absolute;
    display: flex;
    align-items: center;
    gap: 7px;
    font-family: "Arimo", Arial, sans-serif;
    font-weight: 700;
    color: var(--ink);
    letter-spacing: -0.5px;
    white-space: nowrap;
  }
  .brand__dot {
    display: block;
    border-radius: 50%;
    background: var(--orange);
    flex: none;
  }
  .card--front .brand { left: 30px; top: 44px; font-size: 33px; }
  .card--front .brand__dot { width: 36px; height: 36px; }

  .website {
    position: absolute;
    right: 38px;
    top: 33px;
    font-family: "Arimo", Arial, sans-serif;
    font-weight: 700;
    font-size: 15px;
    letter-spacing: 1.4px;
    color: var(--orange);
  }
  .person {
    position: absolute;
    left: 121px;
    top: 132px;
    font-family: "Arimo", Arial, sans-serif;
  }
  .person__name {
    font-size: 31px;
    font-weight: 700;
    color: var(--orange);
    letter-spacing: -0.3px;
    line-height: 1;
    margin-bottom: 10px;
  }
  .person__line {
    font-size: 16px;
    font-weight: 700;
    color: var(--ink);
    letter-spacing: 0.6px;
    line-height: 22px;
  }
  .tagline {
    position: absolute;
    font-family: "Questrial", "Century Gothic", sans-serif;
    color: var(--tagline);
    white-space: nowrap;
  }
  .card--front .tagline { left: 12px; bottom: 11px; font-size: 11.6px; }

  .card--back .brand {
    left: 50%;
    top: 110px;
    transform: translateX(-50%);
    font-size: 40px;
  }
  .card--back .brand__dot { width: 44px; height: 44px; }
  .card--back .tagline {
    left: 0;
    right: 0;
    top: 178px;
    text-align: center;
    font-size: 9.4px;
  }
</style>
</head>
<body>
<main class="stage">
  <section class="card card--front" aria-label="Business card front">
    <svg class="front-art" viewBox="0 0 442 270" aria-hidden="true">
      <defs>
        <linearGradient id="frontWash" x1="0" y1="0" x2="1" y2="0.35">
          <stop offset="0" stop-color="var(--orange)"/>
          <stop offset="0.45" stop-color="var(--orange)" stop-opacity="0.85"/>
          <stop offset="1" stop-color="var(--orange-soft)" stop-opacity="0.15"/>
        </linearGradient>
        <linearGradient id="stripFade" x1="0" y1="0" x2="0" y2="1">
          <stop offset="0" stop-color="#ffffff" stop-opacity="0"/>
          <stop offset="1" stop-color="#ffffff" stop-opacity="0.9"/>
        </linearGradient>
      </defs>
      <rect width="442" height="270" fill="url(#frontWash)"/>
      <rect x="0" y="90" width="58" height="180" fill="url(#stripFade)"/>
      <rect x="58" y="60" width="384" height="210" fill="#ffffff"/>
      <circle cx="63" cy="66" r="48" fill="#ffffff"/>
    </svg>
    <div class="brand"><span class="brand__dot"></span><span class="brand__name">Brightpath</span></div>
    <p class="website">www.brightpath.co.uk</p>
    <div class="person">
      <h1 class="person__name">Linda Marrowby</h1>
      <p class="person__line person__email">lmarrowby@brightpath.co.uk</p>
      <p class="person__line person__phone">07862 413057</p>
    </div>
    <p class="tagline">coaching and mentoring, businesses, colleges and private training providers.</p>
  </section>

  <section class="card card--back" aria-label="Business card back">
    <div class="brand"><span class="brand__dot"></span><span class="brand__name">Brightpath</span></div>
    <p class="tagline">coaching and mentoring, businesses, colleges and private training providers.</p>
  </section>
</main>
</body>
</html>
```